5th Battalion 42nd Cavalry Regiment " Grey Falcons"

Hello,
I am a lieutenant in the Northmark Defense Corps and my boss lieutenant colonel (commander) has asked me to come up with a business card for him. I threw a few designs toward him and he declined all of them. He really like the Knight business card background that is attached below(, but would like another Knight to replace it). We are 5th Battalion 42nd Cavalry Regiment (Grey Falcons is are Battalion Symbol) and are a Heavy Armored Combat team( Tanks and Carver's). He is an Infantry LTC would love a Bold but simple Grey Falcon riding on a horse. It doesn’t have to have the same back ground as the attached file named Finished Card, but will need all the information that is on both sides of the card. Thank you very much for your help and I look forward to seeing the designs.
V/R
Dale Whitcombe

Reason: My boss would like to see a few more designs.

```html
<!DOCTYPE html>
<html lang="en">
<head>
<meta charset="utf-8">
<title>Grey Falcons – Battalion Commander Card</title>
<link rel="stylesheet" href="https://fonts.googleapis.com/css2?family=Marcellus+SC&display=swap">
<style>
  :root {
    --ink: #000000;
    --paper: #ffffff;
    --gold: #d6ac4f;
    --gold-line: #b98d35;
    --white: #f4f4f4;
    --tan-light: #d9c39a;
    --tan-dark: #7d6441;
    --bronze-light: #8a6f4c;
    --bronze-dark: #120d08;
  }
  * { box-sizing: border-box; margin: 0; padding: 0; }
  html, body {
    width: 1029px; height: 1200px; overflow: hidden;
    background: var(--paper);
  }
  body {
    font-family: "Marcellus SC", "Copperplate", serif;
    color: var(--white);
    position: relative;
  }
  .card-side {
    position: absolute; left: 0; width: 1029px;
    background: var(--ink);
  }
  .card-front { top: 0; height: 575px; }
  .card-back { top: 622px; height: 578px; }

  .ruled-title {
    position: absolute; left: 0; width: 100%;
    display: flex; align-items: center; gap: 18px;
    white-space: nowrap;
  }
  .ruled-title::before, .ruled-title::after {
    content: ""; flex: 1; height: 3px; background: currentColor;
  }
  .unit-title { top: 22px; font-size: 37px; color: var(--gold); letter-spacing: 1px; }
  .unit-title::before, .unit-title::after { background: var(--gold-line); }

  .mission {
    position: absolute; top: 84px; left: 20px; right: 20px;
    text-align: center; font-size: 31px; line-height: 37px; letter-spacing: 0.5px;
  }
  .vehicle { position: absolute; }
  .vehicle-ifv { left: 47px; top: 251px; width: 326px; height: 227px; }
  .vehicle-tank { left: 525px; top: 280px; width: 461px; height: 175px; }

  .motto {
    position: absolute; top: 474px; width: 100%;
    text-align: center; font-size: 30px; letter-spacing: 0.5px;
  }
  .battle-cry {
    position: absolute; top: 514px; width: 100%;
    text-align: center; font-size: 44px; color: var(--gold); letter-spacing: 1px;
  }

  .commander-name { top: 38px; font-size: 46px; letter-spacing: 1px; }
  .commander-role { top: 95px; font-size: 35px; letter-spacing: 1px; }
  .commander-name::before { flex: 0 0 150px; }
  .commander-role::before { flex: 0 0 210px; }
  .regiment {
    position: absolute; top: 148px; left: 58px;
    font-size: 39px; color: var(--gold); letter-spacing: 1px; white-space: nowrap;
  }

  .emblem {
    position: absolute; left: 40px; top: 250px;
    display: flex; align-items: center; gap: 14px;
    font-size: 34px; color: var(--gold);
  }
  .emblem-mark { width: 34px; height: 34px; background: var(--gold); }

  .rider-art { position: absolute; left: 402px; top: 241px; width: 627px; height: 337px; }

  .contact {
    position: absolute; left: 26px; top: 410px;
    list-style: none; font-size: 30px; line-height: 38.5px; letter-spacing: 0.5px;
  }
  .contact .email { font-size: 25px; }
</style>
</head>
<body>
  <section class="card-side card-front">
    <h1 class="ruled-title unit-title">Grey Falcons Unit Division</h1>
    <p class="mission">A superbly fit, trained, disciplined, ready and adaptable unit, exercising mission command and teamwork to agressively execute any mission and win!</p>
    <svg class="vehicle vehicle-ifv" role="img" aria-label="Tracked infantry fighting vehicle in desert tan" viewBox="0 0 326 227">
      <defs><linearGradient id="ifvTone" x1="0" y1="0" x2="0" y2="1">
        <stop offset="0" stop-color="var(--tan-light)"/><stop offset="1" stop-color="var(--tan-dark)"/>
      </linearGradient></defs>
      <rect x="0" y="40" width="326" height="187" rx="30" fill="url(#ifvTone)" opacity="0.85"/>
    </svg>
    <svg class="vehicle vehicle-tank" role="img" aria-label="Main battle tank in desert tan" viewBox="0 0 461 175">
      <defs><linearGradient id="tankTone" x1="0" y1="0" x2="0" y2="1">
        <stop offset="0" stop-color="var(--tan-light)"/><stop offset="1" stop-color="var(--tan-dark)"/>
      </linearGradient></defs>
      <rect x="0" y="20" width="461" height="155" rx="40" fill="url(#tankTone)" opacity="0.85"/>
    </svg>
    <p class="motto">Always towards the enemy</p>
    <p class="battle-cry">STRIKE FIRST</p>
  </section>

  <section class="card-side card-back">
    <h2 class="ruled-title commander-name">LTC MARCUS T. DELVANE</h2>
    <p class="ruled-title commander-role">BATTALION COMMANDER</p>
    <p class="regiment">5th Battalion, 42nd CAVALRY REGIMENT</p>
    <div class="emblem">
      <span class="emblem-mark"></span>
      <span class="emblem-name">Grey Falcons</span>
    </div>
    <svg class="rider-art" role="img" aria-label="Armoured rider with lance on a rearing horse, bronze toned" viewBox="0 0 627 337">
      <defs><radialGradient id="riderTone" cx="0.55" cy="0.35" r="0.7">
        <stop offset="0" stop-color="var(--bronze-light)"/><stop offset="1" stop-color="var(--bronze-dark)"/>
      </radialGradient></defs>
      <rect width="627" height="337" fill="url(#riderTone)"/>
    </svg>
    <ul class="contact">
      <li>Work: 555.240.0183</li>
      <li>BB: 555.250.0147</li>
      <li>Cell: 555.720.0162</li>
      <li class="email">marcus.t.delvane.mil@mail.example</li>
    </ul>
  </section>
</body>
</html>
```